New Hotel Showcase Website

We plan to launch a website called www.brindlestays.net which showcases the world’s best new hotels. We want a mock up for 2 pages: the homepage (page 1) and the individual hotel page (page 2). We are looking for a design which combines simplicity while highlighting images/features of the hotel. Because the theme of the site is new hotels it is important that the design somehow emphasizes the age of each hotel listed – both on the homepage and then on the individual hotel page.

NOTE: WE WANT A CREATIVE, NEW APPROACH TO DISPLAYING HOTELS. NOT JUST A COPY OF CURRENT HOTEL WEBSITES.

The design should consider unique and creative ways of helping users to navigate the homepage (page 1) based on the age, location or style of the hotel they are interested in. The individual hotel page(page 2) can be more standard by clearly setting out hotel photos, feature lists, reviews, contact details and potential discounts. There is no booking system needed as this is not a hotel booking website.

The design should ideally be compatible with a content management system such as Page Loom. In terms of reference materials we like sites similar to:

http://www.velmarquay.net
http://www.corvidandpine.net
http://www.tessarooms.net
http://www.quillbeds.net

These sites are designed far more simply than large booking sites such as www.roamvix.net, www.bunkfold.net or even wander ledger. However, we are not looking for a copy of the above. We are looking for a design that presents hotels in a novel way and would be seen by the industry as a unique way of displaying new hotels.
Updates

Dear Designers - we have received quite a few entries already. Thank you. However, none of the designs submitted have responded to our brief. They are all copies or derivatives of current hotel websites which is not what we are looking for. We want (a) a new and creative approach to a hotel website and (b) one which creatively uses the age of the hotel (ie. 1 month old, 6 months old etc).

It will require creative thinking and new ideas. We wanted to challenge designers to come up with something new. Thanks.

```html
<!DOCTYPE html>
<html lang="en">
<head>
<meta charset="utf-8">
<title>Brindlestays — World Best New Hotels</title>
<link href="https://fonts.googleapis.com/css2?family=Questrial&display=swap" rel="stylesheet">
<style>
  :root {
    --orange: #e8832a;
    --orange-light: #f3a43a;
    --orange-deep: #d06a1e;
    --ink: #1f1f1f;
    --dial-face: #ebeae5;
    --dial-rim: #dcdad3;
    --white: #ffffff;
    --photo-a: #3f7fd0;
    --photo-b: #8fbbe6;
  }
  * { margin: 0; padding: 0; box-sizing: border-box; }
  html, body { width: 1200px; height: 764px; overflow: hidden; background: var(--white); }
  body { position: relative; font-family: "Questrial", sans-serif; color: var(--ink); }

  .header-rule { position: absolute; top: 86px; height: 2px; background: var(--orange); }
  .header-rule--left { left: 55px; width: 46px; }
  .header-rule--right { left: 397px; width: 748px; }

  .brand { position: absolute; left: 120px; top: 58px; width: 262px; height: 42px; }
  .brand__mark { position: absolute; left: 0; top: 8px; width: 26px; height: 26px; background: var(--orange); }
  .brand__name { position: absolute; left: 36px; top: 0; width: 220px; height: 42px; overflow: visible; }
  .brand__name text { font-family: "Questrial", sans-serif; font-size: 31px; fill: var(--ink); }

  .main-nav a {
    position: absolute; top: 71px; font-size: 13px; color: var(--ink);
    text-decoration: none; letter-spacing: 0.3px; padding-bottom: 3px; white-space: nowrap;
  }
  .main-nav a.is-active { border-bottom: 2px solid var(--ink); }
  .nav-home { left: 676px; }
  .nav-about { left: 747px; }
  .nav-signin { left: 845px; }
  .nav-booking { left: 936px; }
  .nav-contact { left: 1034px; }

  .headline { position: absolute; left: 410px; top: 128px; width: 706px; height: 66px; overflow: visible; }
  .headline text { font-family: "Questrial", sans-serif; font-size: 56px; filter: drop-shadow(2px 3px 2px rgba(0,0,0,0.3)); }

  .slider { position: absolute; left: 176px; top: 233px; width: 848px; height: 314px; }
  .slider__photo { width: 100%; height: 100%; background: linear-gradient(135deg, var(--photo-a), var(--photo-b)); }
  .slider__arrow { position: absolute; top: 142px; width: 22px; height: 34px; }
  .slider__arrow--prev { left: -40px; }
  .slider__arrow--next { right: -40px; }
  .slider__dots { position: absolute; right: 22px; bottom: 13px; display: flex; gap: 8px; }
  .slider__dot { width: 10px; height: 10px; border-radius: 50%; background: var(--orange); }
  .slider__dot.is-current { background: var(--white); }

  .finder-band {
    position: absolute; left: 55px; top: 630px; width: 1090px; height: 60px;
    background: linear-gradient(180deg, var(--orange-light) 0%, var(--orange) 55%, var(--orange-deep) 100%);
  }
  .finder-prompt { position: absolute; left: 565px; top: 640px; width: 180px; height: 42px; overflow: visible; }
  .finder-prompt text { font-family: "Questrial", sans-serif; font-size: 17px; fill: var(--white); }
  .finder-user { position: absolute; left: 754px; top: 641px; width: 37px; height: 37px; }

  .dial { position: absolute; top: 572px; width: 176px; height: 176px; }
  .dial--location { left: 112px; }
  .dial--age { left: 347px; }
  .dial text { font-family: "Questrial", sans-serif; fill: var(--orange-deep); font-size: 6px; text-anchor: middle; }
  .dial .dial__title { fill: var(--ink); font-size: 13px; letter-spacing: 2px; }
</style>
</head>
<body>
  <div class="header-rule header-rule--left"></div>
  <div class="header-rule header-rule--right"></div>

  <div class="brand">
    <span class="brand__mark"></span>
    <svg class="brand__name" viewBox="0 0 220 42" role="img" aria-label="Brindlestays">
      <text x="0" y="32" textLength="218" lengthAdjust="spacingAndGlyphs">BRINDLESTAYS</text>
    </svg>
  </div>

  <nav class="main-nav">
    <a href="#" class="nav-home is-active">HOME</a>
    <a href="#" class="nav-about">ABOUT US</a>
    <a href="#" class="nav-signin">SIGN IN</a>
    <a href="#" class="nav-booking">BOOKING</a>
    <a href="#" class="nav-contact">CONTACT</a>
  </nav>

  <h1 class="headline">
    <svg width="706" height="66" viewBox="0 0 706 66" role="img" aria-label="World Best New Hotels">
      <defs>
        <linearGradient id="headlineFill" x1="0" y1="0" x2="0" y2="1">
          <stop offset="0%" stop-color="#f3a43a"/><stop offset="100%" stop-color="#d06a1e"/>
        </linearGradient>
      </defs>
      <text x="2" y="54" fill="url(#headlineFill)" textLength="698" lengthAdjust="spacingAndGlyphs">WORLD BEST NEW HOTELS</text>
    </svg>
  </h1>

  <section class="slider">
    <div class="slider__photo" role="img" aria-label="Photo of a resort infinity pool with palm trees and sun loungers"></div>
    <svg class="slider__arrow slider__arrow--prev" viewBox="0 0 22 34"><path d="M18 2 L4 17 L18 32" fill="none" stroke="var(--orange)" stroke-width="2.5"/></svg>
    <svg class="slider__arrow slider__arrow--next" viewBox="0 0 22 34"><path d="M4 2 L18 17 L4 32" fill="none" stroke="var(--orange)" stroke-width="2.5"/></svg>
    <div class="slider__dots">
      <span class="slider__dot is-current"></span>
      <span class="slider__dot"></span>
      <span class="slider__dot"></span>
      <span class="slider__dot"></span>
      <span class="slider__dot"></span>
    </div>
  </section>

  <div class="finder-band"></div>

  <svg class="dial dial--location" viewBox="0 0 176 176">
    <defs>
      <radialGradient id="dialShade" cx="50%" cy="45%" r="55%">
        <stop offset="80%" stop-color="#efeee9"/><stop offset="100%" stop-color="#cfcdc6"/>
      </radialGradient>
    </defs>
    <circle cx="88" cy="88" r="87" fill="url(#dialShade)"/>
    <circle cx="88" cy="88" r="76" fill="var(--dial-face)" stroke="var(--orange)" stroke-width="2"/>
    <g stroke="var(--orange)" stroke-width="0.8" opacity="0.7">
      <line x1="88" y1="12" x2="88" y2="164"/>
      <line x1="12" y1="88" x2="164" y2="88"/>
      <line x1="34" y1="34" x2="142" y2="142"/>
      <line x1="142" y1="34" x2="34" y2="142"/>
    </g>
    <circle cx="88" cy="88" r="37" fill="var(--dial-rim)" stroke="var(--orange)" stroke-width="1"/>
    <circle cx="88" cy="88" r="30" fill="#e3e1db"/>
    <text class="dial__title" x="88" y="86">HOTEL</text>
    <text class="dial__title" x="88" y="99" style="letter-spacing:0.5px;font-size:12px">LOCATION</text>
    <text x="65" y="33">NORTH</text><text x="65" y="40">AMERICA</text>
    <text x="110" y="37">EUROPE</text>
    <text x="142" y="66">MIDDLE</text><text x="142" y="73">EAST</text>
    <text x="143" y="106">NORTH</text><text x="143" y="113">ASIA</text>
    <text x="110" y="140">SOUTH</text><text x="110" y="147">ASIA</text>
    <text x="68" y="144">AUSTRALIA</text>
    <text x="35" y="110">AFRICA</text>
    <text x="33" y="66">SOUTH</text><text x="33" y="73">AMERICA</text>
  </svg>

  <svg class="dial dial--age" viewBox="0 0 176 176">
    <circle cx="88" cy="88" r="87" fill="url(#dialShade)"/>
    <circle cx="88" cy="88" r="76" fill="var(--dial-face)" stroke="var(--orange)" stroke-width="2"/>
    <g stroke="var(--orange)" stroke-width="0.8" opacity="0.7">
      <line x1="88" y1="12" x2="88" y2="164"/>
      <line x1="12" y1="88" x2="164" y2="88"/>
    </g>
    <circle cx="88" cy="88" r="42" fill="var(--dial-rim)" stroke="var(--orange)" stroke-width="1"/>
    <circle cx="88" cy="88" r="30" fill="#e3e1db"/>
    <text class="dial__title" x="88" y="84">TIME</text>
    <text class="dial__title" x="88" y="98" style="letter-spacing:0.5px">OPEN</text>
    <text x="44" y="46">NEXT</text><text x="44" y="53">YEAR</text>
    <text x="128" y="46">JUST</text><text x="128" y="53">OPEN</text>
    <text x="44" y="128">THIS</text><text x="44" y="135">YEAR</text>
    <text x="130" y="126">TWO TO SIX</text><text x="130" y="133">MONTHS</text>
  </svg>

  <svg class="finder-prompt" viewBox="0 0 180 42" role="img" aria-label="Please select hotel location and age">
    <text x="0" y="16" textLength="175" lengthAdjust="spacingAndGlyphs">PLEASE SELECT HOTEL</text>
    <text x="0" y="35" textLength="176" lengthAdjust="spacing">LOCATION&#160; AND&#160; AGE</text>
  </svg>
  <svg class="finder-user" viewBox="0 0 37 37" aria-label="Account">
    <circle cx="18.5" cy="18.5" r="18.5" fill="var(--white)"/>
    <circle cx="18.5" cy="14" r="5" fill="var(--ink)"/>
    <path d="M9 27 Q9 20 18.5 20 Q28 20 28 27 Z" fill="var(--ink)"/>
  </svg>
</body>
</html>
```